Business Card Design Project

We have a logo, but would like to expand the use of it into a business card design. We are a B2B technology exchange platform for institutional investors to invest excess cash into short term assets matching their credit and pricing parameters. The assets are fractionalized and investors invest in portions.

Our customers are large, institutional, financial companies who are a bit traditional. We are high energy rebels with a cause...we are a disruptive technology and want to be viewed as a game changer but we need to present an image of trustworthiness and secure.

We are open not only to the image design but the material, die cut, etc. but want to stay in the traditional size of a business card.

We have other formats of the logo if needed. Our website is www.brambleharbor.com

I have posted a powerpoint template that we have been using.  This should not be considered the template we will use (after business cards we will have another project to incorporate business card design into powerpoint template) but just to give you a flavor of where we have been and have used in the past.

Target Market(s)

Institutional investors, asset managers, large fund institutions

Industry/Entity Type

Financial

Requirements
Must have
• Our logo
Traditional size
Nice to have
• unique use of logo, unique material, die cut, etc
Crisp, clean look
Use of both sides of card in a creative manner

```html
<!DOCTYPE html>
<html lang="en">
<head>
<meta charset="utf-8">
<title>Bramble Harbor – Business Card</title>
<link rel="stylesheet" href="https://fonts.googleapis.com/css2?family=Open+Sans:wght@300;400;600&display=swap">
<style>
  :root {
    --stage: #3a4350;
    --card: #221f1e;
    --card-edge: #3a2a28;
    --accent: #f29a1f;
    --accent-soft: #e88d17;
    --mark-grey: #5b5857;
    --url-grey: #c9c6c2;
  }
  * { box-sizing: border-box; margin: 0; padding: 0; }
  html, body { width: 1200px; height: 900px; overflow: hidden; }
  body {
    background: var(--stage);
    font-family: "Open Sans", sans-serif;
    display: flex;
    flex-direction: column;
    align-items: center;
    justify-content: center;
    gap: 48px;
  }
  .card {
    width: 560px;
    height: 320px;
    background: var(--card);
    border: 1px solid var(--card-edge);
    border-radius: 22px;
    box-shadow: 0 10px 28px rgba(0,0,0,.45);
    position: relative;
    color: var(--accent);
  }
  /* back side */
  .card-back {
    display: flex;
    flex-direction: column;
    justify-content: center;
    padding-left: 60px;
  }
  .card-back .site-url {
    font-size: 31px;
    font-weight: 400;
    letter-spacing: 3px;
    color: var(--url-grey);
  }
  .card-back .tagline {
    margin-top: 10px;
    font-size: 13px;
    font-weight: 400;
    color: var(--accent);
  }
  /* front side */
  .brand {
    position: absolute;
    left: 40px;
    top: 150px;
    display: flex;
    align-items: center;
    gap: 12px;
  }
  .brand-dot {
    width: 44px; height: 44px;
    border-radius: 50%;
    background: var(--accent);
  }
  .brand-name {
    font-size: 30px;
    font-weight: 600;
    color: var(--mark-grey);
    letter-spacing: 1px;
  }
  .contact {
    position: absolute;
    left: 300px;
    top: 40px;
  }
  .contact .person {
    font-size: 19px;
    font-weight: 400;
    margin-bottom: 14px;
  }
  .contact ul { list-style: none; }
  .contact li {
    display: flex;
    align-items: center;
    gap: 8px;
    font-size: 13.5px;
    line-height: 21px;
  }
  .contact svg { width: 12px; height: 12px; flex: none; }
  .address {
    position: absolute;
    left: 40px;
    bottom: 30px;
    font-size: 12px;
    color: var(--accent-soft);
  }
</style>
</head>
<body>
  <section class="card card-back">
    <p class="site-url">www.brambleharbor.com</p>
    <p class="tagline">Higher short yields. Your specific credit and pricing criteria.</p>
  </section>

  <section class="card card-front">
    <div class="brand">
      <span class="brand-dot"></span>
      <span class="brand-name">Bramble Harbor</span>
    </div>
    <div class="contact">
      <p class="person">Martin Ellory, CEO</p>
      <ul>
        <li>
          <svg viewBox="0 0 12 12"><path d="M3 1 L5 3.5 L3.8 5 Q5 7.5 7 8.2 L8.5 7 L11 9 L9.5 11 Q4 10.5 1 3 Z" fill="var(--accent)"/></svg>
          +805.555.0142
        </li>
        <li>
          <svg viewBox="0 0 12 12"><rect x="0.5" y="2" width="11" height="8" fill="var(--accent)"/><path d="M0.5 2 L6 6.5 L11.5 2" stroke="var(--card)" fill="none" stroke-width="1"/></svg>
          mellory@brambleharbor.com
        </li>
        <li>
          <svg viewBox="0 0 12 12"><circle cx="6" cy="6" r="5" fill="none" stroke="var(--accent)" stroke-width="1.3"/><path d="M1 6 H11 M6 1 Q3 6 6 11 Q9 6 6 1" fill="none" stroke="var(--accent)" stroke-width="1"/></svg>
          www.BrambleHarbor.com
        </li>
        <li>
          <svg viewBox="0 0 12 12"><circle cx="6" cy="6" r="5.5" fill="var(--accent)"/></svg>
          martinellory
        </li>
      </ul>
    </div>
    <p class="address">2180 Harbor Crest Drive, Suite 410, Fairview Bay, CA 90210</p>
  </section>
</body>
</html>
```